Visitenkarten-Design für Autowerkstatt/-verwertung
Zielgruppe
Unser Unternehmen besteht aus zwei Bereiche:
- Autoverwertung
- Autowerkstatt
Aufgabenstellung
Informationen auf der Visitenkarte:
'Brunnhofer' - Logo
Lindenauer Str. 31
80993 München
Autoverwertung Autoteile
www.autoverwertung-brunnhofer-beispiel.de
info@autoverwertung-brunnhofer-beispiel.de
Autowerkstatt
www.auto-brunnhofer-beispiel.de
info@auto-brunnhofer-beispiel.de
Öffnungszeiten:
Mo-Fr
08.00 - 12.00 Uhr und 13.00 - 17.00 Uhr
Farblich sollte die Visitenkarte sich an das Logo anpassen. Visitenkarte 2-4 seitig.

```html
<!DOCTYPE html>
<html lang="de">
<head>
<meta charset="utf-8">
<title>Brunnhofer – Visitenkarten</title>
<link rel="stylesheet" href="https://fonts.googleapis.com/css2?family=Arimo:ital,wght@0,400;0,700;1,400;1,700&display=swap">
<style>
  :root {
    --bg: #d6d5d1;
    --white: #ffffff;
    --red: #c8101a;
    --dark: #545655;
    --mid: #7d7e7e;
    --light: #dcdddd;
    --ink: #3f4142;
    --paper-shadow: 0 6px 14px rgba(0,0,0,.22);
  }
  * { box-sizing: border-box; margin: 0; padding: 0; }
  html, body { width: 1000px; height: 1200px; overflow: hidden; }
  body { background: var(--bg); font-family: "Arimo", Arial, sans-serif; color: var(--ink); position: relative; }

  .card { position: absolute; background: var(--white); box-shadow: var(--paper-shadow); overflow: hidden; }

  /* Front card */
  .card--front { left: 300px; top: 90px; width: 410px; height: 265px; }
  .card--front .brand { position: absolute; left: 34px; top: 36px; display: flex; align-items: center; gap: 12px; }
  .brand__dot { width: 34px; height: 34px; border-radius: 50%; background: var(--red); flex: none; }
  .brand__name { font-weight: 700; font-size: 46px; color: var(--ink); letter-spacing: -0.5px; }
  .card--front .band { position: absolute; left: 0; right: 0; top: 112px; bottom: 0; background: var(--dark); border-top: 3px solid var(--red); }
  .card--front .services { position: absolute; left: 24px; top: 14px; font-style: italic; font-size: 15px; line-height: 18px; color: var(--white); }
  .hours { position: absolute; left: 20px; top: 64px; color: var(--white); font-weight: 700; font-size: 15px; line-height: 18px; }
  .hours__grid { display: grid; grid-template-columns: 70px auto; margin-top: 8px; }
  .card--front .art { position: absolute; right: 0; top: 0; bottom: 0; width: 140px; background: radial-gradient(circle at 55% 55%, #6e6f6f, var(--mid)); }

  /* Folded inside card */
  .card--inside { left: 90px; top: 400px; width: 820px; height: 265px; }
  .panel { position: absolute; top: 0; bottom: 0; }
  .panel--left { left: 0; width: 300px; }
  .panel--center { left: 300px; width: 240px; background: linear-gradient(#dcdddd 0 70%, #4f5150 70% 100%); }
  .panel--right { left: 540px; width: 280px; }
  .panel__top { position: absolute; left: 0; right: 0; top: 0; height: 190px; }
  .panel__bottom { position: absolute; left: 0; right: 0; top: 190px; bottom: 0; background: var(--dark); border-top: 3px solid var(--red); padding: 16px 16px 0 20px; color: var(--white); font-style: italic; font-size: 12.5px; line-height: 20px; white-space: nowrap; }
  .panel--right .panel__bottom { text-align: right; padding: 16px 20px 0 16px; }
  .section-title { position: absolute; font-weight: 700; color: var(--red); font-size: 30px; line-height: 30px; padding-bottom: 4px; border-bottom: 2px solid var(--red); }
  .panel--left .section-title { left: 24px; top: 34px; padding-right: 10px; }
  .panel--right .section-title { right: 0; top: 44px; padding-right: 22px; width: 210px; text-align: right; }
  .phone-label { position: absolute; font-weight: 700; font-size: 19px; color: var(--ink); }
  .phone { position: absolute; font-weight: 700; font-size: 27px; color: var(--ink); letter-spacing: .5px; white-space: nowrap; }
  .panel--left .phone-label { left: 30px; top: 116px; }
  .panel--left .phone { left: 28px; top: 142px; }
  .panel--right .phone-label { right: 26px; top: 120px; }
  .panel--right .phone { right: 24px; top: 146px; }

  /* Back card */
  .card--back { left: 270px; top: 770px; width: 410px; height: 265px; }
  .back__info { position: absolute; left: 0; top: 0; bottom: 0; width: 195px; background: var(--dark); color: var(--white); }
  .back__name { position: absolute; left: 26px; top: 34px; font-weight: 700; font-style: italic; font-size: 26px; }
  .back__rule { position: absolute; left: 0; top: 70px; width: 150px; height: 2px; background: var(--red); }
  .back__services { position: absolute; left: 30px; top: 86px; font-style: italic; font-size: 15px; line-height: 18px; }
  .back__address { position: absolute; left: 26px; top: 186px; font-weight: 700; font-size: 18px; line-height: 24px; white-space: nowrap; }
  .back__map { position: absolute; left: 220px; top: 22px; width: 168px; height: 150px; background: linear-gradient(135deg, #f4f4f4, #e2e2e2); border: 1px solid #cfcfcf; }
  .back__brand { position: absolute; left: 222px; top: 200px; display: flex; align-items: center; gap: 7px; }
  .back__brand .brand__dot { width: 16px; height: 16px; }
  .back__brand .brand__name { font-size: 21px; }
</style>
</head>
<body>

<section class="card card--front" aria-label="Vorderseite">
  <div class="brand"><span class="brand__dot"></span><span class="brand__name">Brunnhofer</span></div>
  <div class="band">
    <p class="services">Autoverwertung<br>Autowerkstatt</p>
    <div class="hours">
      <p>Öffnungszeiten:</p>
      <div class="hours__grid">
        <span>Mo – Fr</span><span>08.00 – 12.00 Uhr</span>
        <span>und</span><span>13.00 – 17.00 Uhr</span>
      </div>
    </div>
    <div class="art" role="img" aria-label="Werkzeug-Symbol mit Zahnrad in Grautönen"></div>
  </div>
</section>

<section class="card card--inside" aria-label="Innenseite">
  <div class="panel panel--left">
    <div class="panel__top">
      <h2 class="section-title">Autoverwertung<br>Autoteile</h2>
      <p class="phone-label">Telefon</p>
      <p class="phone">0 89 - 41 62 90 53</p>
    </div>
    <div class="panel__bottom">www.autoverwertung-brunnhofer-beispiel.de<br>info@autoverwertung-brunnhofer-beispiel.de</div>
  </div>
  <div class="panel panel--center" role="img" aria-label="Große, blasse Werkzeug- und Zahnrad-Grafik"></div>
  <div class="panel panel--right">
    <div class="panel__top">
      <h2 class="section-title">Autowerkstatt</h2>
      <p class="phone-label">Mobil</p>
      <p class="phone">0160 - 52 48 37 1</p>
    </div>
    <div class="panel__bottom">www.auto-brunnhofer-beispiel.de<br>info@auto-brunnhofer-beispiel.de</div>
  </div>
</section>

<section class="card card--back" aria-label="Rückseite">
  <div class="back__info">
    <p class="back__name">Brunnhofer</p>
    <span class="back__rule"></span>
    <p class="back__services">Autverwertung<br>Autoteile<br>Autoteile<br>Autowerkstatt</p>
    <p class="back__address">Lindenauer Str. 31<br>80993 München</p>
  </div>
  <div class="back__map" role="img" aria-label="Lageplan mit Straßen und Standortmarkierung"></div>
  <div class="back__brand"><span class="brand__dot"></span><span class="brand__name">Brunnhofer</span></div>
</section>

</body>
</html>
```